Tandrew Advisory Group Business Card Design Project

2-sided business card for my small (me and a couple subcontractors) firm, which consults to public community colleges and school districts and public agencies in California on energy matters, mostly solar electric systems that can reduce their electricity use by as much as 80%. I prepare requests for proposals (RFPs), manage the RFP processes, and work with the solar vendors to get the best deal for my clients. I also do regulatory and legislative advocacy for strong renewable energy policies. I do lots of quantitative analysis to make sure the solar systems are sized to produce the maximum monetary savings and focus a lot on the aesthetic design of the solar systems, as architectural features of the campuses (most are carport structures built in parking lots, but some are built on the ground and on rooftops). All my work is geared to getting the best value, highest quality, and most reliable solar system. My career background is in public interest energy advocacy; I'm not a consultant trying to make a million dollars but someone who is still serving in the public interest.

My competition is made up of much larger firms; this business card/logo in large part is intended to present an image of my firm as an equal to these larger firms despite my smaller size.

Essential information as follows:
Firm name: Tandrew Advisory Group
Tagline: Clean Energy Procurement for the Public Sector
Name: Gavin Tandrew
email, 2 phone number, and address listed as well.

Target Market(s)

Public schools, community colleges, & public agencies.There is a wide range in the sophistication of these organizations.

Industry/Entity Type

Parking

Requirements
Must have
• - several rich colors, which can be either in the logo or in the background - the overall feeling of the card should reflect richness of color. I have uploaded some photos showing some colors that I like together. By rich I do not necessarily mean bright. I suppose bright colors in the logo could be supported with rich colors in the overall background of the card.
- professional, and powerful in an understated way (not kooky, cartoonish, or very playful)
- the logo must NOT be too representational of solar energy or the sun, but at the same time it would be good for the logo to be somewhat suggestive of this.

Nice to have
• -I like abstract and geometric images (with rich colts).
- A very subtle reference to schools/colleges/education would be great but it CANNOT be explicit; it would have to be faintly suggestive.
- In the logo I like the idea of abstract or geometric shapes intersecting with other in an interesting and suggestive way, conveying the multiple aspects of my practice (economics, data analysis, energy analysis, problem solving, managing collaborative processes, policy analysis)
- My work relates to environmental concerns, especially climate change. Working this into the logo in a subtle way could be good, but it's not a requirement.
- I like the idea that the logo/card feels serene.
- In designing the business card, I kind of like the idea of having the tag line as the first thing they read, then they see the firm name.

Should not have
• Not:
- humorous
- boring
- overly slick
- overly formal
- whimsical

```html
<!DOCTYPE html>
<html lang="en">
<head>
<meta charset="utf-8">
<title>Tandrew Advisory Group – Business Card</title>
<link rel="stylesheet" href="https://fonts.googleapis.com/css2?family=Jost:wght@400;600&display=swap">
<style>
  :root {
    --backdrop: #2b2f33;
    --card-white: #f7f7f5;
    --ink: #3a3a3a;
    --ink-soft: #555555;
    --rule: #b9b9b9;
    --brand-blue: #1f95c9;
    --brand-green: #22a24a;
    --teal: #1b8a8c;
    --band-light: rgba(255, 255, 255, 0.16);
    --on-dark: #ffffff;
    --on-dark-soft: rgba(255, 255, 255, 0.85);
  }
  * { box-sizing: border-box; margin: 0; padding: 0; }
  html, body {
    width: 1200px; height: 800px; overflow: hidden;
    background: var(--backdrop);
    font-family: "Jost", "Century Gothic", sans-serif;
  }
  .canvas {
    width: 1200px; height: 800px;
    display: flex; align-items: center; justify-content: center; gap: 60px;
  }
  .card {
    position: relative;
    width: 525px; height: 300px;
    overflow: hidden;
    box-shadow: 0 10px 30px rgba(0,0,0,0.35);
  }

  /* Front */
  .card--front { background: var(--card-white); color: var(--ink); }
  .front__brand {
    position: absolute; left: 36px; top: 44px;
    display: flex; align-items: center; gap: 12px;
  }
  .brand-mark {
    width: 22px; height: 22px; background: var(--brand-green);
  }
  .front__name-mark {
    font-size: 22px; font-weight: 400; color: var(--ink);
    letter-spacing: 0.02em; line-height: 1.1; max-width: 200px;
  }
  .tagline {
    position: absolute; right: 30px; top: 42px;
    font-size: 14px; line-height: 1.25; color: var(--ink);
    width: 190px;
  }
  .front__details {
    position: absolute; left: 36px; right: 24px; bottom: 46px;
    display: flex; align-items: flex-end; gap: 16px;
  }
  .person__name {
    font-size: 17px; font-weight: 600; letter-spacing: 0.03em;
    text-transform: uppercase;
  }
  .person__title { font-size: 14px; color: var(--ink-soft); }
  .divider { width: 1px; height: 44px; background: var(--rule); }
  .contact { list-style: none; font-size: 13px; color: var(--ink-soft); }
  .contact li { display: flex; align-items: center; gap: 8px; line-height: 1.55; }
  .contact svg { width: 12px; height: 12px; fill: none; stroke: var(--brand-blue); stroke-width: 1.6; }
  .address { font-size: 13px; line-height: 1.4; color: var(--ink-soft); font-style: normal; }
  .front__stripe-blue {
    position: absolute; left: 0; right: 0; bottom: 14px; height: 8px;
    background: var(--brand-blue);
  }
  .front__stripe-green {
    position: absolute; left: 0; right: 0; bottom: 0; height: 14px;
    background: var(--brand-green);
  }

  /* Back */
  .card--back {
    background: linear-gradient(160deg, var(--brand-blue) 0%, var(--teal) 40%, var(--brand-green) 100%);
    color: var(--on-dark);
  }
  .back__band {
    position: absolute; left: 0; right: 0; top: 96px; height: 104px;
    background: var(--band-light);
    display: flex; align-items: center; justify-content: space-between;
    padding: 0 30px;
  }
  .back__brand { display: flex; align-items: center; gap: 12px; }
  .back__brand .brand-mark { background: var(--on-dark); }
  .back__name-mark {
    font-size: 22px; font-weight: 400; color: var(--on-dark);
    letter-spacing: 0.02em; line-height: 1.1; max-width: 200px;
  }
  .back__tagline { font-size: 14px; line-height: 1.25; color: var(--on-dark-soft); width: 190px; }
</style>
</head>
<body>
<main class="canvas">
  <section class="card card--front" aria-label="Business card front">
    <div class="front__brand">
      <span class="brand-mark" aria-hidden="true"></span>
      <span class="front__name-mark">Tandrew Advisory Group</span>
    </div>
    <p class="tagline">Clean Energy Procurement for the Public Sector</p>

    <div class="front__details">
      <div class="person">
        <p class="person__name">Gavin Tandrew</p>
        <p class="person__title">General Manager</p>
      </div>
      <span class="divider"></span>
      <ul class="contact">
        <li>
          <svg viewBox="0 0 12 12" aria-hidden="true"><rect x="3" y="0.8" width="6" height="10.4" rx="1"/><line x1="5.2" y1="9.3" x2="6.8" y2="9.3"/></svg>
          (916) 555-0148
        </li>
        <li>
          <svg viewBox="0 0 12 12" aria-hidden="true"><rect x="0.8" y="2.5" width="10.4" height="7" rx="0.5"/><polyline points="0.8,2.5 6,6.6 11.2,2.5"/></svg>
          info@tandrewag.com
        </li>
      </ul>
      <span class="divider"></span>
      <address class="address">1450 Alder Park Ave.<br>Sacramento, CA 95814</address>
    </div>

    <div class="front__stripe-blue"></div>
    <div class="front__stripe-green"></div>
  </section>

  <section class="card card--back" aria-label="Business card back">
    <div class="back__band">
      <div class="back__brand">
        <span class="brand-mark" aria-hidden="true"></span>
        <span class="back__name-mark">Tandrew Advisory Group</span>
      </div>
      <p class="back__tagline">Clean Energy Procurement for the Public Sector</p>
    </div>
  </section>
</main>
</body>
</html>
```